The Lantern Den Business Cards

We are a Craft Beer/Upscale dining Bar/Restaurant. We'll have 24 taps of craft beers and several types of bottled beers. In addition, we'll be serving a variety of top shelf bourbons, spirits and wines with a small unique menu. I'd like the design to be sophisticated, elegant and modern while staying away from "cartoonish" pictures.
Updates
Hello, I've added some example logos for inspiration. I'd like to use a lot of black/white with maybe a little color for a "pop". Thank you!
Industry/Entity Type
Business
Contact Information for Business Card
THE LANTERN DEN
Tomas Orlikova
582 Wexmoor Street
Norfolk, Virginia 23847
Office: (757) 555-0143
Mobile: (757) 555-0178
Look and feel
Each slider illustrates characteristics of the customer's brand and the style your logo design should communicate.

```html
<!DOCTYPE html>
<html lang="en">
<head>
<meta charset="utf-8">
<title>The Lantern Den – Business Card</title>
<link href="https://fonts.googleapis.com/css2?family=Lato:wght@400;700;900&display=swap" rel="stylesheet">
<style>
  :root {
    --backdrop: #3a2a1d;
    --card-black: #0e0e0e;
    --card-edge: #1a1a1a;
    --ink-light: #e4e4e4;
    --ink-white: #f5f5f5;
    --accent-red: #e3262b;
  }
  * { margin: 0; padding: 0; box-sizing: border-box; }
  html, body {
    width: 1200px;
    height: 900px;
    overflow: hidden;
    background: var(--backdrop);
    font-family: "Lato", sans-serif;
  }
  .stage {
    width: 1200px;
    height: 900px;
    display: flex;
    align-items: center;
    justify-content: center;
  }
  .business-card {
    position: relative;
    width: 840px;
    height: 480px;
    background: var(--card-black);
    border: 1px solid var(--card-edge);
    box-shadow: 0 18px 40px rgba(0, 0, 0, 0.45);
    color: var(--ink-light);
  }
  .brand-name {
    position: absolute;
    top: 130px;
    left: 0;
    width: 100%;
    text-align: center;
    font-weight: 700;
    font-size: 52px;
    letter-spacing: 1px;
    color: var(--ink-light);
  }
  .tagline {
    position: absolute;
    top: 262px;
    left: 0;
    width: 100%;
    text-align: center;
    font-weight: 700;
    font-size: 21px;
    letter-spacing: 1.5px;
    color: var(--ink-white);
  }
  .tagline .separator {
    color: var(--accent-red);
    margin: 0 14px;
  }
  .contact-name {
    position: absolute;
    top: 342px;
    left: 80px;
    font-weight: 400;
    font-size: 33px;
    letter-spacing: 1px;
    color: var(--accent-red);
  }
  .phone-list {
    position: absolute;
    top: 312px;
    left: 470px;
    list-style: none;
    font-size: 24px;
    line-height: 34px;
  }
  .phone-list .label {
    display: inline-block;
    width: 118px;
    color: var(--accent-red);
  }
  .phone-list .number { color: var(--ink-white); }
  .address {
    position: absolute;
    top: 410px;
    left: 0;
    width: 100%;
    text-align: center;
    font-size: 24px;
    color: var(--ink-white);
  }
</style>
</head>
<body>
  <main class="stage">
    <article class="business-card">
      <h1 class="brand-name">THE LANTERN DEN</h1>
      <p class="tagline">CRAFT BEER<span class="separator">•</span>CRAFT COCKTAILS<span class="separator">•</span>FINE DINING</p>
      <p class="contact-name">TOMAS ORLIKOVA</p>
      <ul class="phone-list">
        <li><span class="label">Office :</span><span class="number">(757) 555-0143</span></li>
        <li><span class="label">Mobile :</span><span class="number">(757) 555-0178</span></li>
      </ul>
      <p class="address">582 Wexmoor Street Norfolk, Virginia 23847</p>
    </article>
  </main>
</body>
</html>
```